Banner Pop Up Opt In Form REDESIGNS - SLEEK BLACK LOOK

Please redesign banners attached.

I am looking for a very sleek look....I do not like this collage of images on these current designs. Please keep all content same but use images that pop.

I have an acccount at www.pixmorrow-example.com or you can use your own images.

I like black background for somereason because it looks very sleek....but these designs should pop , build trust and credibility and have easy opt in form....SLEEK AND MODERN LOOK is what im looking for....

Target Market(s)

Consumers on websites

Requirements
Must have
• Please redesign banners attached.

Nice to have

Should not have

```html
<!DOCTYPE html>
<html lang="en">
<head>
<meta charset="utf-8">
<title>Resort Opt-In Banners</title>
<link rel="stylesheet" href="https://fonts.googleapis.com/css2?family=Bebas+Neue&family=Poppins:wght@400;600&display=swap">
<style>
  :root {
    --page-bg: #e6e6e6;
    --panel-black: #0d0d0d;
    --accent-blue: #1e8fd6;
    --headline-blue: #1597ea;
    --offer-yellow: #ffd400;
    --text-white: #ffffff;
    --field-border: #f2f2f2;
    --veil: rgba(20, 20, 20, 0.45);
  }
  * { box-sizing: border-box; margin: 0; padding: 0; }
  html, body {
    width: 1200px; height: 583px; overflow: hidden;
    background: var(--page-bg);
  }
  .canvas { position: relative; width: 1200px; height: 583px; }
  .banner {
    position: absolute; top: 64px;
    width: 530px; height: 455px; overflow: hidden;
    background: var(--panel-black);
  }
  .banner--offer { left: 54px; }
  .banner--win { left: 616px; }
  .banner__photo {
    position: absolute; inset: 0;
    background: linear-gradient(180deg,
      #cfe3f2 0%, #a9cbe4 22%, #8bb3c9 34%,
      #3f7a3a 44%, #2f6a2a 56%, #5b4436 66%,
      #b8582c 80%, #8e3d1f 100%);
  }
  .banner__shape { position: absolute; inset: 0; width: 530px; height: 455px; }
  .banner__content {
    position: absolute; left: 23px; top: 0; width: 300px; height: 455px;
    color: var(--text-white);
  }
  .headline-kicker {
    position: absolute; top: 26px; left: 0;
    font-family: "Bebas Neue", sans-serif;
    font-size: 44px; line-height: 1; color: var(--headline-blue);
  }
  .headline-main {
    position: absolute; top: 56px; left: -2px;
    font-family: "Bebas Neue", sans-serif;
    font-size: 108px; line-height: 1; color: var(--text-white);
  }
  .lead {
    position: absolute; top: 152px; left: 0; width: 240px;
    font-family: "Poppins", sans-serif;
    font-size: 11.3px; line-height: 15px; text-transform: uppercase;
  }
  .prize {
    position: absolute; top: 201px; left: 0; width: 260px;
    font-family: "Bebas Neue", sans-serif;
    font-size: 34px; line-height: 29px; color: var(--offer-yellow);
  }
  .optin-form { position: absolute; top: 262px; left: 0; width: 180px; }
  .optin-field {
    display: block; height: 30px; margin-bottom: 7.5px;
    border: 1.5px solid var(--field-border); border-radius: 3px;
    font-family: "Poppins", sans-serif; font-size: 11.5px;
    line-height: 27px; padding-left: 8px; color: var(--text-white);
    background: rgba(0,0,0,0.35);
  }
  .optin-submit {
    display: block; height: 30px; margin-top: 1px;
    background: var(--accent-blue); border-radius: 3px;
    font-family: "Poppins", sans-serif; font-weight: 600;
    font-size: 12px; line-height: 30px; padding-left: 9px;
  }
  .fine-print {
    position: absolute; top: 425px; left: 0; width: 190px;
    font-family: "Poppins", sans-serif; font-size: 7.9px; line-height: 9.5px;
  }
</style>
</head>
<body>
<main class="canvas">

  <section class="banner banner--offer">
    <div class="banner__photo" role="img" aria-label="Resort terrace with palm trees, infinity pool, wicker lounger and sea view"></div>
    <svg class="banner__shape" viewBox="0 0 530 455" aria-hidden="true">
      <polygon points="222,0 290,0 338,251 290,455 232,455 292,251" fill="var(--veil)"/>
      <polygon points="0,0 205,0 275,251 215,455 0,455" fill="var(--panel-black)" fill-opacity="0.93"/>
      <polygon points="205,0 222,0 292,251 232,455 215,455 275,251" fill="var(--accent-blue)"/>
    </svg>
    <div class="banner__content">
      <h2 class="headline-kicker">Want a great</h2>
      <h1 class="headline-main">OFFER</h1>
      <p class="lead">Subscribe to our newsletter and recieve a complimentary</p>
      <p class="prize">7 Night Resort/ Condo-<br>3500 + Locations</p>
      <div class="optin-form">
        <span class="optin-field">NAME</span>
        <span class="optin-field">EMAIL</span>
        <span class="optin-field">PHONE</span>
        <span class="optin-submit">SUBMIT</span>
      </div>
      <p class="fine-print">We will send an email and a text message the offer and instruction how to redeem</p>
    </div>
  </section>

  <section class="banner banner--win">
    <div class="banner__photo" role="img" aria-label="Resort terrace with palm trees, infinity pool, wicker lounger and sea view"></div>
    <svg class="banner__shape" viewBox="0 0 530 455" aria-hidden="true">
      <polygon points="222,0 290,0 338,251 290,455 232,455 292,251" fill="var(--veil)"/>
      <polygon points="0,0 205,0 275,251 215,455 0,455" fill="var(--panel-black)" fill-opacity="0.93"/>
      <polygon points="205,0 222,0 292,251 232,455 215,455 275,251" fill="var(--accent-blue)"/>
    </svg>
    <div class="banner__content">
      <h2 class="headline-kicker">Enter to</h2>
      <h1 class="headline-main">WIN</h1>
      <p class="lead">Subscribe to our newsletter and recieve a complimentary</p>
      <p class="prize">7 Night Resort/ Condo-<br>3500 + Locations</p>
      <div class="optin-form">
        <span class="optin-field">NAME</span>
        <span class="optin-field">EMAIL</span>
        <span class="optin-field">PHONE</span>
        <span class="optin-submit">SUBMIT</span>
      </div>
      <p class="fine-print">We will send an email and a text message the offer and instruction how to redeem</p>
    </div>
  </section>

</main>
</body>
</html>
```